Real Estate Card Design

I need a new business card! Below you will find my headshot, the company logo and a copy of my previous business card.

The card must contain the following information:

Dana Welch
Sales Representative
FAIR HARBOUR HOMES REALTY INC BROKERGE
204-517 Maple Ave E, Oshawa ON L1G 4K7
Cell: 905-618-4037 Office:905-481-2696
www.danawelch.com dana@movewithwelch.ca

I would like the card to portray security and class all the while being fresh and contemporary. I hold the key....

```html
<!DOCTYPE html>
<html lang="en">
<head>
<meta charset="utf-8">
<title>Dana Welch – Business Card</title>
<link rel="stylesheet" href="https://fonts.googleapis.com/css2?family=Source+Sans+3:wght@400;600&display=swap">
<style>
  :root {
    --page: #ffffff;
    --panel-grey: #464646;
    --panel-dark: #111a17;
    --blue-light: #00a3e6;
    --blue-deep: #0066b8;
    --teal-dark: #063b45;
    --teal-mid: #0a7f99;
    --text-light: #ffffff;
    --text-dark: #111111;
    --rule-blue: #2aa9e0;
  }
  html, body {
    margin: 0;
    width: 1200px;
    height: 1200px;
    overflow: hidden;
    background: var(--page);
    font-family: "Source Sans 3", "Myriad Pro", sans-serif;
  }
  .card {
    position: absolute;
    left: 22px;
    top: 253px;
    width: 1156px;
    height: 694px;
    overflow: hidden;
  }
  .card-art {
    position: absolute;
    inset: 0;
    width: 100%;
    height: 100%;
    display: block;
  }
  .agent-name {
    position: absolute;
    left: 81px;
    top: 118px;
    margin: 0;
    color: var(--text-light);
    font-weight: 400;
    line-height: 0.92;
    letter-spacing: 1px;
  }
  .agent-name .first { display: block; font-size: 60px; }
  .agent-name .last { display: block; font-size: 72px; letter-spacing: 2px; }
  .agent-title {
    position: absolute;
    left: 92px;
    top: 243px;
    margin: 0;
    padding: 0 4px;
    border-left: 1.5px solid var(--rule-blue);
    border-right: 1.5px solid var(--rule-blue);
    color: var(--text-light);
    font-size: 19px;
    line-height: 22px;
    letter-spacing: -0.2px;
  }
  .contact-list {
    position: absolute;
    left: 81px;
    top: 316px;
    margin: 0;
    padding: 0;
    list-style: none;
  }
  .contact-item {
    display: flex;
    align-items: center;
    height: 58px;
    margin-bottom: 27px;
  }
  .contact-icon {
    width: 59px;
    height: 58px;
    flex: none;
    display: block;
  }
  .contact-text {
    margin-left: 23px;
    color: var(--text-light);
    font-size: 21px;
    line-height: 29px;
    white-space: nowrap;
  }
  .contact-text .label { display: inline-block; width: 63px; }
  .brokerage {
    position: absolute;
    left: 626px;
    top: 23px;
    width: 214px;
    height: 214px;
    border-radius: 50%;
    background: var(--text-light);
    display: flex;
    flex-direction: column;
    align-items: center;
    justify-content: center;
    text-align: center;
    color: var(--text-dark);
    font-weight: 600;
  }
  .brokerage .line-main { font-size: 21px; line-height: 22px; }
  .brokerage .line-sub { font-size: 11px; line-height: 14px; letter-spacing: 1px; margin-top: 3px; }
  .brokerage .line-tiny { font-size: 6px; letter-spacing: 3px; line-height: 9px; }
</style>
</head>
<body>
<main class="card">
  <svg class="card-art" viewBox="35 407 1862 1117" preserveAspectRatio="none" aria-hidden="false">
    <defs>
      <linearGradient id="blueStripe" x1="0" y1="0" x2="0" y2="1">
        <stop offset="0" stop-color="var(--blue-light)"/>
        <stop offset="1" stop-color="var(--blue-deep)"/>
      </linearGradient>
      <linearGradient id="tealShard" x1="0" y1="0" x2="0" y2="1">
        <stop offset="0" stop-color="var(--teal-dark)"/>
        <stop offset="1" stop-color="var(--teal-mid)"/>
      </linearGradient>
      <radialGradient id="portraitTone" cx="0.55" cy="0.35" r="0.8">
        <stop offset="0" stop-color="#6b5a4c"/>
        <stop offset="0.45" stop-color="#2a2b33"/>
        <stop offset="1" stop-color="#111a17"/>
      </radialGradient>
    </defs>
    <rect class="panel-dark" x="35" y="407" width="1862" height="1117" fill="var(--panel-dark)"/>
    <rect class="portrait" role="img" aria-label="Portrait of the agent in a pinstripe suit holding up a house key"
          x="1330" y="595" width="567" height="929" fill="url(#portraitTone)"/>
    <polygon class="panel-grey" points="35,407 655,407 960,1020 1250,1524 35,1524" fill="var(--panel-grey)"/>
    <polygon class="shard-teal" points="1035,1040 1120,1050 1345,1524 1252,1524" fill="url(#tealShard)"/>
    <polygon class="stripe-top" points="655,407 797,407 1115,1057 960,1022" fill="url(#blueStripe)"/>
    <polygon class="stripe-lower" points="1082,858 1185,882 1500,1524 1410,1524" fill="url(#blueStripe)"/>
  </svg>

  <h1 class="agent-name"><span class="first">DANA</span><span class="last">WELCH</span></h1>
  <p class="agent-title">SALES REPRESENTATIVE</p>

  <ul class="contact-list">
    <li class="contact-item">
      <svg class="contact-icon" viewBox="0 0 59 58">
        <rect width="59" height="58" fill="var(--blue-light)"/>
        <polygon points="59,0 59,58 0,58" fill="var(--blue-deep)" opacity="0.35"/>
        <path d="M16 24c0-5 6-7 13.5-7S43 19 43 24v3h-6v-3h-15v3h-6z" fill="#fff"/>
        <path d="M20 29h19l3 11H17z" fill="#fff"/>
        <g fill="var(--blue-light)">
          <rect x="24" y="31" width="3" height="2"/><rect x="28" y="31" width="3" height="2"/><rect x="32" y="31" width="3" height="2"/>
          <rect x="24" y="35" width="3" height="2"/><rect x="28" y="35" width="3" height="2"/><rect x="32" y="35" width="3" height="2"/>
        </g>
      </svg>
      <div class="contact-text"><span class="label">Cell:</span>905-618-4037<br>Office: 905-481-2696</div>
    </li>
    <li class="contact-item">
      <svg class="contact-icon" viewBox="0 0 59 58">
        <rect width="59" height="58" fill="var(--blue-light)"/>
        <polygon points="59,0 59,58 0,58" fill="var(--blue-deep)" opacity="0.35"/>
        <circle cx="29" cy="28" r="12" fill="none" stroke="#fff" stroke-width="2.5"/>
        <path d="M19 22c6 2 14 2 20 6M22 37c2-6 8-12 16-16M27 16c-3 6-3 16 2 24" fill="none" stroke="#fff" stroke-width="2"/>
        <path d="M36 35l7 3-3 1 2 3-2 1-2-3-2 2z" fill="#fff"/>
      </svg>
      <div class="contact-text">www.danawelch.com<br>dana@movewithwelch.ca</div>
    </li>
    <li class="contact-item">
      <svg class="contact-icon" viewBox="0 0 59 58">
        <rect width="59" height="58" fill="var(--blue-light)"/>
        <polygon points="59,0 59,58 0,58" fill="var(--blue-deep)" opacity="0.35"/>
        <path d="M29.5 14c-6 0-10.5 4.5-10.5 10.5 0 8 10.5 19.5 10.5 19.5S40 32.5 40 24.5C40 18.5 35.5 14 29.5 14z" fill="#fff"/>
        <circle cx="29.5" cy="24.5" r="4" fill="var(--blue-light)"/>
      </svg>
      <div class="contact-text">204-517 Maple Ave E,<br>Oshawa ON L1G 4K7</div>
    </li>
  </ul>

  <div class="brokerage">
    <span class="line-main">FAIR HARBOUR<br>HOMES</span>
    <span class="line-sub">REALTY INC</span>
    <span class="line-tiny">BROKERGE</span>
  </div>
</main>
</body>
</html>
```